Plakat-Design
Zielgruppe
Wir sind ein Hotelunternehmen und eröffnen einen neuen Standort mit einem Boutique-Hotel. Die Zielgruppe sind Hotelgäste.
Aufgabenstellung
Wir benötigen ein Plakat mit den Maßen 6x4 m (siehe Bild anbei) für unsseren neuen Standort.
Farben Schwarz Weiss
Das Haus wird noch komplett weiß eingekleidet für die spätere Enthüllung und dann kommt das Plakat drüber
TEXT:
Großes Logo Hotel
Wir machen Lustenau noch schöner
Hier entsteht unser Boutique Hotel
Aus der Firmengruppe der Feldkontor (als Logo)
Bild von Greta Hulsen mit dem untertext: Greta Hulsen, Geschäftsführerin Business Hotel Hulsen

```html
<!DOCTYPE html>
<html lang="de">
<head>
<meta charset="utf-8">
<title>Hulsen Boutique Hotel – Bauplakat</title>
<link rel="stylesheet" href="https://fonts.googleapis.com/css2?family=Montserrat:wght@300;400;500;700&display=swap">
<style>
  :root {
    --ink: #1a1a1a;
    --paper: #ffffff;
    --stage: #e9e9e7;
    --rule: #8a8a8a;
    --portrait-light: #d4d4d4;
    --portrait-dark: #8f8f8f;
    --band: #1b1b1b;
  }
  * { margin: 0; padding: 0; box-sizing: border-box; }
  html, body { width: 1200px; height: 1200px; overflow: hidden; }
  body {
    background: var(--stage);
    font-family: "Montserrat", sans-serif;
    color: var(--ink);
    position: relative;
  }
  .poster {
    position: absolute;
    left: 30px; top: 220px;
    width: 1140px; height: 760px;
    background: var(--paper);
    overflow: hidden;
  }
  .portrait {
    position: absolute;
    left: 0; top: 0;
    width: 539px; height: 664px;
    background: linear-gradient(160deg, var(--portrait-light) 0%, #b5b5b5 55%, var(--portrait-dark) 100%);
  }
  .portrait-caption {
    position: absolute;
    left: 54px; top: 588px;
    color: var(--paper);
    text-transform: uppercase;
  }
  .portrait-caption .name {
    font-size: 15px; font-weight: 500; letter-spacing: 2px;
  }
  .portrait-caption .role {
    font-size: 9px; font-weight: 400; letter-spacing: 0.8px; line-height: 1.3; margin-top: 4px;
  }
  .brand {
    position: absolute;
    right: 65px; top: 60px;
    text-align: right;
  }
  .brand-name {
    display: block;
    font-size: 150px; font-weight: 400; line-height: 1;
    letter-spacing: -2px;
  }
  .brand-sub {
    display: block;
    margin-top: 22px;
    font-size: 36px; font-weight: 500; letter-spacing: 6px;
  }
  .rule {
    position: absolute;
    left: 579px; right: 0;
    height: 2px;
    background: var(--rule);
  }
  .rule.top { top: 359px; }
  .rule.bottom { top: 589px; }
  .headline {
    position: absolute;
    right: 65px; top: 376px;
    text-align: right;
    text-transform: uppercase;
    line-height: 1.12;
  }
  .headline .light { display: block; font-size: 46px; font-weight: 400; }
  .headline .strong { display: block; font-size: 66px; font-weight: 700; line-height: 1.05; }
  .group-mark {
    position: absolute;
    right: 62px; top: 608px;
    font-size: 28px; font-weight: 700;
    letter-spacing: -0.5px;
  }
  .band {
    position: absolute;
    left: 0; bottom: 0;
    width: 100%; height: 96px;
    background: var(--band);
    color: var(--paper);
    display: flex; align-items: center; justify-content: center;
    font-size: 34px; font-weight: 500; letter-spacing: 5px;
    text-transform: uppercase;
  }
</style>
</head>
<body>
  <main class="poster">
    <div class="portrait" role="img" aria-label="Schwarz-Weiß-Porträt der Geschäftsführerin Greta Hulsen in weißer Bluse vor grauem Hintergrund"></div>
    <div class="portrait-caption">
      <p class="name">Greta Hulsen</p>
      <p class="role">Geschäftsführerin<br>Business Hotel Hulsen</p>
    </div>

    <div class="brand">
      <span class="brand-name">Hulsen</span>
      <span class="brand-sub">Boutique Hotel</span>
    </div>

    <div class="rule top"></div>
    <h1 class="headline">
      <span class="light">Wir machen</span>
      <span class="strong">Lustenau</span>
      <span class="light">noch schöner</span>
    </h1>
    <div class="rule bottom"></div>

    <p class="group-mark">Feldkontor</p>

    <footer class="band">Hier entsteht unser Boutique Hotel</footer>
  </main>
</body>
</html>
```